Larkfield Capital Webinar Ads

Need a banner pack in less than 48 hours for this website:
http://larkfieldcapital-demo.com/webinar
Target Market(s)
Accredited real estate investors looking to grow their portfolio
Font styles to use
Sans Serif
Colors
0255a3
f37123
000000

```html
<!DOCTYPE html>
<html lang="en">
<head>
<meta charset="utf-8">
<title>Larkfield Capital Webinar Ads</title>
<link href="https://fonts.googleapis.com/css2?family=Ubuntu:wght@400;500;700&family=Oswald:wght@500&display=swap" rel="stylesheet">
<style>
:root{
  --bg:#3b2a1e;
  --brand-blue:#0255a3;
  --deep-blue:#0a2a6b;
  --headline:#f7d117;
  --white:#ffffff;
  --orange:#f37123;
  --black:#000000;
  --go-top:#ffd23a;
  --go-bottom:#f09a00;
  --logo-ink:#3d3d3d;
  --panel:#f4f4f4;
}
*{box-sizing:border-box;margin:0;padding:0}
html,body{width:1200px;height:955px;overflow:hidden}
body{background:var(--bg);position:relative;font-family:'Ubuntu',sans-serif}
.banner{position:absolute;overflow:hidden;box-shadow:0 3px 8px rgba(0,0,0,.55);background:var(--deep-blue)}
.photo{position:absolute;inset:0;background:radial-gradient(ellipse at 50% 30%,#2f6fc4 0%,var(--brand-blue) 35%,var(--deep-blue) 100%)}
.content{position:relative;z-index:1;height:100%;display:flex}
.logo{background:var(--panel);display:flex;align-items:center;justify-content:center;color:var(--logo-ink);font-weight:500;text-align:center;line-height:1.1}
.headline{color:var(--headline);font-weight:700;text-align:center;line-height:1.2}
.body-copy{color:var(--white);text-align:center;line-height:1.2;font-weight:400}
.register{font-family:'Oswald',sans-serif;color:var(--orange);text-align:center;line-height:1.05;font-weight:500}
.go{display:inline-flex;align-items:center;justify-content:center;gap:4px;border-radius:999px;background:linear-gradient(var(--go-top),var(--go-bottom));color:#1a1a1a;font-weight:700;border:1px solid #b06e00}
.go svg{fill:#1a1a1a}
.stack{flex-direction:column}
.mid{flex:1;display:flex;flex-direction:column;justify-content:center;align-items:center}
.cta-dark{background:linear-gradient(#1a1a1a,var(--black));display:flex;flex-direction:column;align-items:center;justify-content:center}
.foot{background:var(--panel);display:flex;align-items:center;justify-content:space-between;padding:0 14px}
.foot .cta{display:flex;flex-direction:column;align-items:center;gap:6px}
.sizes{position:absolute;left:391px;top:873px;width:809px;height:82px;background:rgba(0,0,0,.75);display:flex;align-items:center;padding-left:10px;color:var(--white);font-weight:700}
.sizes .label{font-size:34px;margin-right:14px}
.sizes .list{font-size:24px;line-height:1.2}
</style>
</head>
<body>

<!-- 728x90 -->
<section class="banner" style="left:25px;top:21px;width:830px;height:102px">
  <div class="photo" role="img" aria-label="Blurred conference audience in blue tones"></div>
  <div class="content">
    <div class="logo" style="width:171px;font-size:17px">Larkfield Capital</div>
    <div class="mid" style="gap:4px">
      <p class="headline" style="font-size:20px">Discover How Investors Across The Country<br>Are Profiting In This Great Investment Market</p>
      <p class="body-copy" style="font-size:17px">LEARN HOW EASY IT IS TO PROFIT IN THIS<br>GEAT MARKET BEFORE VALUES GO BACK UP...</p>
    </div>
    <div class="cta-dark" style="width:135px;gap:6px">
      <p class="register" style="font-size:21px">REGISTER FOR<br>THE WEBINAR</p>
      <span class="go" style="width:62px;height:24px;font-size:15px">GO<svg width="8" height="10" viewBox="0 0 8 10"><path d="M0 0L8 5L0 10Z"/></svg></span>
    </div>
  </div>
</section>

<!-- 468x60 -->
<section class="banner" style="left:25px;top:140px;width:534px;height:68px">
  <div class="photo" role="img" aria-label="Blurred conference audience in blue tones"></div>
  <div class="content">
    <div class="logo" style="width:112px;font-size:12px">Larkfield Capital</div>
    <div class="mid" style="gap:2px">
      <p class="headline" style="font-size:12.5px">Discover How Investors Across The Country<br>Are Profiting In This Great Investment Market</p>
      <p class="body-copy" style="font-size:11px">LEARN HOW EASY IT IS TO PROFIT IN THIS<br>GEAT MARKET BEFORE VALUES GO BACK UP...</p>
    </div>
    <div class="cta-dark" style="width:80px;gap:3px">
      <p class="register" style="font-size:13px">REGISTER FOR<br>THE WEBINAR</p>
      <span class="go" style="width:40px;height:15px;font-size:10px">GO<svg width="5" height="7" viewBox="0 0 8 10"><path d="M0 0L8 5L0 10Z"/></svg></span>
    </div>
  </div>
</section>

<!-- 160x600 -->
<section class="banner" style="left:25px;top:226px;width:183px;height:684px">
  <div class="photo" role="img" aria-label="Blurred conference audience in blue tones"></div>
  <div class="content stack">
    <div class="logo" style="height:96px;font-size:17px">Larkfield<br>Capital</div>
    <div class="mid" style="gap:38px;padding:0 6px">
      <p class="headline" style="font-size:20px;line-height:1.35">Discover How Investors Across The Country Are Profiting In This Great Investment Market</p>
      <p class="body-copy" style="font-size:19px;line-height:1.3">LEARN HOW EASY IT IS TO PROFIT IN THIS GEAT MARKET BEFORE VALUES GO BACK UP...</p>
    </div>
    <div class="cta-dark" style="height:129px;gap:10px">
      <p class="register" style="font-size:27px">REGISTER FOR<br>THE WEBINAR</p>
      <span class="go" style="width:92px;height:34px;font-size:21px">GO<svg width="10" height="13" viewBox="0 0 8 10"><path d="M0 0L8 5L0 10Z"/></svg></span>
    </div>
  </div>
</section>

<!-- 120x600 -->
<section class="banner" style="left:226px;top:226px;width:137px;height:684px">
  <div class="photo" role="img" aria-label="Blurred conference audience in blue tones"></div>
  <div class="content stack">
    <div class="logo" style="height:96px;font-size:14px">Larkfield<br>Capital</div>
    <div class="mid" style="gap:36px;padding:0 4px">
      <p class="headline" style="font-size:16px;line-height:1.8">Discover How Investors Across The Country Are Profiting In This Great Investment Market</p>
      <p class="body-copy" style="font-size:15.5px;line-height:1.5">LEARN HOW EASY IT IS TO PROFIT IN THIS GEAT MARKET BEFORE VALUES GO BACK UP...</p>
    </div>
    <div class="cta-dark" style="height:129px;gap:10px">
      <p class="register" style="font-size:23px">REGISTER FOR<br>THE WEBINAR</p>
      <span class="go" style="width:92px;height:34px;font-size:21px">GO<svg width="10" height="13" viewBox="0 0 8 10"><path d="M0 0L8 5L0 10Z"/></svg></span>
    </div>
  </div>
</section>

<!-- 336x280 -->
<section class="banner" style="left:380px;top:226px;width:383px;height:319px">
  <div class="photo" role="img" aria-label="Blurred conference audience in blue tones"></div>
  <div class="content stack">
    <div class="mid" style="gap:18px">
      <p class="headline" style="font-size:23px">Discover How Investors Across<br>The Country Are Profiting In<br>This Great Investment Market</p>
      <p class="body-copy" style="font-size:23px">LEARN HOW EASY IT IS TO<br>PROFIT IN THIS GEAT MARKET<br>BEFORE VALUES GO BACK UP...</p>
    </div>
    <div class="foot" style="height:68px">
      <span class="logo" style="background:none;font-size:16px">Larkfield Capital</span>
      <div class="cta">
        <p class="register" style="font-size:19px">REGISTER FOR THE WEBINAR</p>
        <span class="go" style="width:66px;height:26px;font-size:16px">GO<svg width="8" height="10" viewBox="0 0 8 10"><path d="M0 0L8 5L0 10Z"/></svg></span>
      </div>
    </div>
  </div>
</section>

<!-- 300x250 -->
<section class="banner" style="left:780px;top:226px;width:342px;height:285px">
  <div class="photo" role="img" aria-label="Blurred conference audience in blue tones"></div>
  <div class="content stack">
    <div class="mid" style="gap:14px">
      <p class="headline" style="font-size:20.5px">Discover How Investors Across<br>The Country Are Profiting In<br>This Great Investment Market</p>
      <p class="body-copy" style="font-size:21px">LEARN HOW EASY IT IS TO<br>PROFIT IN THIS GEAT MARKET<br>BEFORE VALUES GO BACK UP...</p>
    </div>
    <div class="foot" style="height:60px">
      <span class="logo" style="background:none;font-size:14px">Larkfield Capital</span>
      <div class="cta" style="gap:4px">
        <p class="register" style="font-size:16px">REGISTER FOR THE WEBINAR</p>
        <span class="go" style="width:60px;height:23px;font-size:14px">GO<svg width="7" height="9" viewBox="0 0 8 10"><path d="M0 0L8 5L0 10Z"/></svg></span>
      </div>
    </div>
  </div>
</section>

<!-- 250x250 -->
<section class="banner" style="left:380px;top:562px;width:285px;height:285px">
  <div class="photo" role="img" aria-label="Blurred conference audience in blue tones"></div>
  <div class="content stack">
    <div class="mid" style="gap:14px">
      <p class="headline" style="font-size:17px">Discover How Investors Across<br>The Country Are Profiting In<br>This Great Investment Market</p>
      <p class="body-copy" style="font-size:17.5px;line-height:1.4">LEARN HOW EASY IT IS TO<br>PROFIT IN THIS GEAT MARKET<br>BEFORE VALUES GO BACK UP...</p>
    </div>
    <div class="foot" style="height:68px;padding:0 10px">
      <span class="logo" style="background:none;font-size:12.5px">Larkfield Capital</span>
      <div class="cta" style="gap:5px">
        <p class="register" style="font-size:14px">REGISTER FOR THE WEBINAR</p>
        <span class="go" style="width:56px;height:22px;font-size:14px">GO<svg width="7" height="9" viewBox="0 0 8 10"><path d="M0 0L8 5L0 10Z"/></svg></span>
      </div>
    </div>
  </div>
</section>

<!-- 200x200 -->
<section class="banner" style="left:683px;top:562px;width:228px;height:228px">
  <div class="photo" role="img" aria-label="Blurred conference audience in blue tones"></div>
  <div class="content stack">
    <div class="mid" style="gap:12px">
      <p class="headline" style="font-size:13.5px">Discover How Investors Across<br>The Country Are Profiting In<br>This Great Investment Market</p>
      <p class="body-copy" style="font-size:14px;line-height:1.35">LEARN HOW EASY IT IS TO<br>PROFIT IN THIS GEAT MARKET<br>BEFORE VALUES GO BACK UP...</p>
    </div>
    <div class="foot" style="height:48px;padding:0 8px">
      <span class="logo" style="background:none;font-size:10.5px">Larkfield Capital</span>
      <div class="cta" style="gap:3px">
        <p class="register" style="font-size:11px">REGISTER FOR THE WEBINAR</p>
        <span class="go" style="width:44px;height:17px;font-size:11px">GO<svg width="6" height="7" viewBox="0 0 8 10"><path d="M0 0L8 5L0 10Z"/></svg></span>
      </div>
    </div>
  </div>
</section>

<div class="sizes">
  <span class="label">Banner Sizes:</span>
  <span class="list">728x90, 468x60, 336x280, 300x250<br>160x600, 120x600, 250x250, 200x200</span>
</div>

</body>
</html>
```